Need a tea box packaging design

* Organic Herbal tea
* Imported from india to france for european community
* our main rivals are " ZENDRA" tea and " BRAVO" tea.
* the product will be sold online and shops.
* 15 variety of teas will be imported.
* The details in the attached file.
The Packaging contents:
Main page :
Brand Name : KORIL ( logo attached)
Name of the product: KELORA THE NOIR ( which means Kelora black tea)
Type of the product : Infusion
No of tea bags : 20
Weight of each bag : 1,5 gm
Total weight : 30 gm
Organic label name : Europe ( organic logo attached)
vegan label : vegan ( vegan label attached)
The other side contents will be given later.
A model that i have designed with another designer is attached. It is nice. But i am expecting more than that. ( attached)
Some designs that i like are attached here.
As mentionned earlier there will 15 variety of teas, so the design should easily modifiable by just changing colours.
Updates
Project Deadline Extended Reason: I think the deadline is very short due to the weekend. So, I feel it is better to extend the deadline by 5 days. Added Saturday, January 21, 2017
Target Market(s)
Europe. Mainly france.
Industry/Entity Type
Community
Requirements
Must have
- * Design should be modern and colourfull.
- * I like pattern works, Vectorials
- * Yoga silouhaites in the design is appreciable.
- * The design should express wellness, joy and love
Nice to have
- "Zendra" tea in my inspirational design.
- * The ingredients can be showed in vectorial designs in the back ground.
- * The end user must see the box while taking the tea and appreciate
- * The end user must search and find some hidden things.
- * The box must be communicative.
- * Trendy frames.
Should not have
- No need to have tea cups

```html
<!DOCTYPE html>
<html lang="fr">
<head>
<meta charset="utf-8">
<title>Koril – Kelora Black Tea</title>
<link href="https://fonts.googleapis.com/css2?family=Berkshire+Swash&family=Roboto+Slab:wght@500&family=Crimson+Text&display=swap" rel="stylesheet">
<style>
  :root {
    --lime: #b3d136;
    --label-black: #0b0b0b;
    --band-green: #a6c52d;
    --brand-green: #8fc03a;
    --ink: #2a2f12;
    --white: #ffffff;
    --bg: #ffffff;
    --ornament-core: #7a3fa0;
    --ornament-mid: #3aa64a;
    --ornament-edge: #2c9ad6;
  }
  html, body { margin: 0; padding: 0; overflow: hidden; background: var(--bg); }
  .canvas { position: relative; width: 1200px; height: 1200px; overflow: hidden; background: var(--bg); }

  .panel { position: absolute; top: 100px; height: 1000px; background: var(--lime); overflow: hidden; }
  .side-panel { left: 110px; width: 370px; }
  .front-panel { left: 480px; width: 610px; }

  .ornament { position: absolute; border-radius: 50%;
    background: radial-gradient(circle, var(--ornament-core) 0%, var(--ornament-mid) 45%, var(--ornament-edge) 72%, rgba(179, 209, 54, 0) 100%); }

  .side-copy { position: absolute; left: 22px; top: 90px; width: 300px;
    font-family: "Crimson Text", serif; font-size: 14.5px; line-height: 1.95; color: var(--ink); }
  .side-copy p { margin: 0 0 18px; }

  .label { position: absolute; left: 60px; top: 150px; width: 490px; height: 700px; background: var(--label-black); }
  .brand { position: absolute; top: 50px; width: 100%; text-align: center;
    font-family: "Roboto Slab", serif; font-weight: 500; font-size: 44px; color: var(--brand-green); }
  .product-title { position: absolute; top: 125px; width: 100%; margin: 0; text-align: center;
    font-family: "Berkshire Swash", cursive; font-weight: 400; color: var(--white); font-size: 94px; line-height: 1.25; }
  .flavour-band { position: absolute; left: 0; right: 0; top: 470px; height: 230px; background: var(--band-green); }
  .flavour-type { margin: 14px 0 0; text-align: center; font-family: "Roboto Slab", serif; font-weight: 500;
    font-size: 27px; letter-spacing: 1.5px; color: var(--label-black); }
  .ingredient-art { position: absolute; left: 60px; top: 70px; width: 370px; height: 140px; border-radius: 60px;
    background: linear-gradient(90deg, #4f9a2c 0%, #6aab35 30%, #cdb690 55%, #d9c08a 80%, #f0d25a 100%); }

  .info-bar { position: absolute; left: 0; right: 0; bottom: 0; height: 130px; background: var(--label-black); }
  .badge { position: absolute; top: 22px; width: 86px; height: 86px; border-radius: 50%; background: var(--band-green); }
  .badge-organic { left: 28px; }
  .badge-vegan { left: 134px; }
  .net-weight { position: absolute; left: 245px; top: 46px; font-family: "Roboto Slab", serif; font-weight: 500;
    font-size: 25px; color: var(--white); }
</style>
</head>
<body>
<main class="canvas">
  <section class="panel side-panel">
    <div class="ornament" role="img" aria-label="Colourful mandala ornament" style="left:190px; top:-140px; width:360px; height:360px;"></div>
    <div class="ornament" role="img" aria-label="Colourful mandala ornament" style="left:-70px; top:720px; width:340px; height:340px;"></div>
    <div class="side-copy">
      <p>Originaire de l'Inde, le Kelora est considéré comme étant la plus sacrée de toutes les herbes. Elle est connue sous le nom de "reine des herbes" en raison de sa particulière capacité de guérison.</p>
      <p>Elle contient de la vitamine C, du fer, du zinc, du calcium, de la chlorophylle et beaucoup d'autres phyto nutriments bénéfiques à notre système digestif. Chargé en antioxydants, le Kelora protège nos cellules contre les dommages oxydatifs. Il contient des propriétés anti-âge. Il renforce également notre système immunitaire et stimule notre métabolisme.</p>
      <p>Nous avons réalisé de sublimes mélanges de Kelora et d'autres produits ayurvédiques pour vous apporter plaisir et bienfaits au corps. Vous pouvez également visiter notre site koril.fr pour plus d'informations concernant les bienfaits de nos thés.</p>
    </div>
  </section>

  <section class="panel front-panel">
    <div class="ornament" role="img" aria-label="Colourful mandala ornament" style="left:-90px; top:-140px; width:420px; height:420px;"></div>
    <div class="ornament" role="img" aria-label="Colourful mandala ornament" style="left:430px; top:60px; width:260px; height:260px;"></div>
    <div class="ornament" role="img" aria-label="Colourful mandala ornament" style="left:-120px; top:480px; width:260px; height:260px;"></div>
    <div class="ornament" role="img" aria-label="Colourful mandala ornament" style="left:470px; top:480px; width:260px; height:260px;"></div>

    <div class="label">
      <div class="brand">Koril</div>
      <h1 class="product-title">Kelora<br>Black Tea</h1>
      <div class="flavour-band">
        <p class="flavour-type">Kelora Black Tea Infusion</p>
        <div class="ingredient-art" role="img" aria-label="Illustration of basil leaves and ginger root with slices"></div>
      </div>
    </div>

    <div class="info-bar">
      <div class="badge badge-organic" role="img" aria-label="Organic certification badge"></div>
      <div class="badge badge-vegan" role="img" aria-label="Vegan certification badge"></div>
      <div class="net-weight">Net. 30g(1,5 g/bag). 20 bags</div>
    </div>
  </section>
</main>
</body>
</html>
```